Connected Building Infrastructure Business needs awesome document templates.

We'd like to have a fresh set of document templates for business letters, documents, and power point presentations. Brindlewood Wiring and Safety works with IT teams, construction firms, and consultants to provide structured cabling, electronic security, and connected building infrastructure services to firms through the state of New York, Massachusetts, and Vermont.

We have recently refreshed our logo and have started some branding and would like to continue the themes already in place. As a result of this project we are looking for

-letter head template
-document template for sales material (contracts and proposals)
-document template for customer documentation and hand outs
-PowerPoint template for customer and internal presentations

Target Market(s)

CIOs, Vice President of IT Facilities, and Security, Small/Medium Size Business Owners, General Contractors

Industry/Entity Type

Business

Font styles to use
Sans Serif

Requirements
Must have
• -letter head template
• -document template for sales material (contracts and proposals)
• -document template for customer documentation and hand outs
• -PowerPoint template for customer and internal presentations
Should not have
• Do not change logo. Can use knockout and/or black and white version of logo if needed.

```html
<!DOCTYPE html>
<html lang="en">
<head>
<meta charset="utf-8">
<title>Brindlewood Wiring and Safety – Letterhead</title>
<link rel="stylesheet" href="https://fonts.googleapis.com/css2?family=Montserrat:wght@700&family=Open+Sans:wght@400;600&display=swap">
<style>
  :root {
    --backdrop: #e9e9e9;
    --paper: #ffffff;
    --ink: #2b2b2b;
    --ink-soft: #555555;
    --brand-green: #1f6a3b;
    --brand-black: #1a1a1a;
    --signature-tone: #d9d9d9;
  }
  * { box-sizing: border-box; margin: 0; padding: 0; }
  html, body {
    width: 1200px; height: 735px; overflow: hidden;
    background: var(--backdrop);
  }
  .canvas {
    width: 1200px; height: 735px;
    display: flex; align-items: center; justify-content: center;
  }
  .letterhead {
    position: relative;
    width: 481px; height: 680px;
    background: var(--paper);
    box-shadow: 0 4px 18px rgba(0,0,0,0.12);
    font-family: "Open Sans", Arial, sans-serif;
    color: var(--ink);
    overflow: hidden;
  }
  .brand {
    position: absolute; top: 52px; left: 44px;
    display: flex; align-items: center; gap: 8px;
  }
  .brand-square {
    width: 14px; height: 14px; background: var(--brand-green);
  }
  .brand-name {
    font-family: "Montserrat", Arial, sans-serif;
    font-weight: 700; font-size: 9px; letter-spacing: 0.08em;
    text-transform: uppercase; color: var(--brand-black);
    line-height: 1.3; max-width: 130px;
  }
  .letter-body {
    position: absolute; top: 178px; left: 44px; width: 370px;
    font-size: 7.4px; line-height: 1.55;
  }
  .date, .recipient { margin-bottom: 0; }
  .recipient { margin-bottom: 11px; }
  .salutation { margin-bottom: 2px; }
  .letter-body p { margin-bottom: 0; }
  .closing { margin-top: 9px; }
  .signature {
    width: 80px; height: 24px; margin-top: 6px;
    background: var(--signature-tone); border-radius: 2px;
  }
  .signer-title {
    font-size: 9px; color: var(--ink-soft); margin-top: 2px;
  }
  .contact-footer {
    position: absolute; right: 36px; bottom: 24px;
    text-align: right; font-size: 6px; line-height: 1.6;
    color: var(--ink-soft);
  }
  .contact-footer .sep { margin: 0 4px; }
  .edge-band {
    position: absolute; left: 0; right: 0; bottom: 0; height: 6px;
    display: flex;
  }
  .edge-band .green { flex: 1; background: var(--brand-green); }
  .edge-band .black { width: 110px; background: var(--brand-black); }
</style>
</head>
<body>
<main class="canvas">
  <article class="letterhead">
    <header class="brand">
      <span class="brand-square"></span>
      <span class="brand-name">Brindlewood Wiring and Safety</span>
    </header>

    <section class="letter-body">
      <div class="date">November 1, 2015</div>
      <div class="recipient">
        Ms. Dana Whitfield<br>
        48 Harrow Mill Road<br>
        Northvale, U.K 24680
      </div>
      <div class="salutation">Dear Ms. Whitfield</div>
      <p>The first paragraph of a typical business letter is used to state the main point of the letter. Begin with a friendly opening, then quickly transition into the purpose of your letter. Use a couple of sentences to explain the purpose, but do not go in to detail until the next paragraph.</p>
      <p>Beginning with the second paragraph, state the supporting details to justify your purpose. These may take the form of background information, statistics or first-hand accounts. A few short paragraphs within the body of the letter should be enough to support your reasoning.</p>
      <p>Finally, in the closing paragraph, briefly restate your purpose and why it is important. If the purpose of your letter is related to your employment, consider ending your letter with your contact information and title if it is not included on letterhead. However, if the purpose is informational, think about closing with gratitude for the reader's time.</p>
      <div class="closing">Sincerely,</div>
      <div class="signature" role="img" aria-label="Handwritten signature of Alan Pierce"></div>
      <div class="signer-title">President</div>
    </section>

    <footer class="contact-footer">
      <div>27 Fenwick Lane Troyburg, NY 12044</div>
      <div>Tel.555.310.0142 / 800.555.0179<span class="sep">|</span>hello@brindlewoodwiring.com<span class="sep">|</span>www.brindlewoodwiring.com</div>
    </footer>

    <div class="edge-band" aria-hidden="true">
      <span class="green"></span>
      <span class="black"></span>
    </div>
  </article>
</main>
</body>
</html>
```